Patient Satisfaction

We are extending our social listening and intelligence platform for Physicians to patient satisfaction app. Our platform monitors social media and review sites and collects, classifies and distilled patient satisfaction into nine Categories - Thoroughness, Answers Q's, Collaborative, Caring, Time Spent, Previous Success, Instruction Clarity, Follow-up and Reputation

The app will have three main states: (1) Home state showing the metric for each category, (2) a detailed page for each Category showing the metric, topics discussed and sites sourced, (3) Leaderboard showing Physicians with best scores.

If you follow our wireframes, please take liberty to extend it. We like the Panelo 6 tiles, but our wireframes fall far short of meeting its coolness and usefulness. For example, we don't have different size tiles, and would live them, or content on the tiles to make them more meaningful. [Note: use KV instead of KV.]
Updates

The designs submitted to date look great, but they reminded me that my instructions were unclear. Feel free to follow the wireframes if you like the UI, but we also welcome your thoughts on UI in addition to look and feel. If you follow our wireframes, please take liberty to extend it. We like the Panelo 6 tile, but our wireframes falls far short of meeting its coolness and usefulness. For example, we don't have different size tiles or content on the tiles to make them more meaningful. If you've submitted designs, please feel free to revise them or submit a different look. And if you haven't submitted designs, please feel free to give us your best thoughts on UI and design.

Target Market(s)

US Physicians

Industry/Entity Type

Media

Font styles to use
Sans Serif

Colors
f37022
5c5c5c
33a6d7

Requirements
Must have
• Home state
Visual icons
Nice to have
• Leaderbaord

```html
<!DOCTYPE html>
<html lang="en">
<head>
<meta charset="utf-8">
<title>Dashboard</title>
<link href="https://fonts.googleapis.com/css2?family=Lato:wght@400;700&display=swap" rel="stylesheet">
<style>
  :root {
    --teal: #16b8a4;
    --page: #eeeeee;
    --white: #ffffff;
    --overall: #ebbf20;
    --overall-edge: #d2a514;
    --bedside: #5dae41;
    --bedside-edge: #4c9634;
    --knowledge: #397dc2;
    --knowledge-edge: #2c68a8;
    --communication: #844a9d;
    --communication-edge: #6d3885;
    --time: #b2ba3c;
    --time-edge: #99a02e;
    --outcome: #d9434a;
    --outcome-edge: #bd3138;
  }
  * { margin: 0; padding: 0; box-sizing: border-box; }
  html, body {
    width: 676px; height: 1200px; overflow: hidden;
    background: var(--page);
    font-family: "Lato", sans-serif;
    font-weight: 400;
    color: var(--white);
  }
  .screen {
    position: relative;
    width: 640px; height: 1136px;
    transform: scale(1.05625);
    transform-origin: 0 0;
    background: var(--page);
  }
  .app-bar {
    position: absolute; left: 0; top: 0; width: 640px; height: 128px;
    background: var(--teal);
  }
  .status-bar {
    position: absolute; left: 0; top: 0; width: 100%; height: 40px;
    font-size: 22px; line-height: 40px;
  }
  .status-left { position: absolute; left: 14px; top: 0; display: flex; align-items: center; gap: 8px; height: 40px; }
  .status-time { position: absolute; left: 0; right: 0; text-align: center; }
  .status-right { position: absolute; right: 12px; top: 0; display: flex; align-items: center; gap: 8px; height: 40px; }
  .title {
    position: absolute; left: 0; right: 0; top: 58px;
    text-align: center; font-size: 32px; font-weight: 400; letter-spacing: 0.5px;
  }
  .menu-icon { position: absolute; left: 30px; top: 66px; }
  .share-icon { position: absolute; left: 570px; top: 60px; }

  .tile {
    position: absolute; text-align: center;
    border-bottom: 5px solid;
  }
  .tile-label {
    position: absolute; left: 0; right: 0;
    font-size: 19px; letter-spacing: 0.3px;
  }
  .overall { left: 20px; top: 149px; width: 600px; height: 397px; background: var(--overall); border-color: var(--overall-edge); }
  .overall .score { position: absolute; left: 0; right: 0; top: 36px; font-size: 25px; }
  .overall .rank { position: absolute; left: 0; right: 0; top: 124px; font-size: 33px; display: flex; justify-content: center; align-items: center; gap: 14px; }
  .overall .comments { position: absolute; left: 0; right: 0; top: 224px; font-size: 18px; display: flex; justify-content: center; align-items: center; gap: 10px; }
  .overall .tile-label { top: 332px; font-size: 25px; }

  .small { top: 566px; width: 187px; height: 285px; }
  .small .tile-label { top: 236px; }
  .small svg { position: absolute; left: 50%; top: 60px; transform: translateX(-50%); }
  .bedside { left: 20px; background: var(--bedside); border-color: var(--bedside-edge); }
  .knowledge { left: 227px; background: var(--knowledge); border-color: var(--knowledge-edge); }
  .communication { left: 433px; background: var(--communication); border-color: var(--communication-edge); }

  .wide { top: 871px; width: 290px; height: 245px; }
  .wide .tile-label { top: 196px; }
  .wide svg { position: absolute; left: 50%; top: 48px; transform: translateX(-50%); }
  .time-spent { left: 20px; background: var(--time); border-color: var(--time-edge); }
  .outcome { left: 330px; background: var(--outcome); border-color: var(--outcome-edge); }
</style>
</head>
<body>
<main class="screen">
  <header class="app-bar">
    <div class="status-bar">
      <div class="status-left">
        <svg width="66" height="14" viewBox="0 0 66 14" fill="none" stroke="#fff" stroke-width="1.5">
          <circle cx="7" cy="7" r="5.5" fill="#fff"/><circle cx="20" cy="7" r="5.5" fill="#fff"/><circle cx="33" cy="7" r="5.5" fill="#fff"/>
          <circle cx="46" cy="7" r="5.5"/><circle cx="59" cy="7" r="5.5"/>
        </svg>
        <span>Novalink</span>
        <svg width="22" height="16" viewBox="0 0 22 16" fill="#fff"><path d="M11 16 L0 4 A16 16 0 0 1 22 4 Z"/></svg>
      </div>
      <div class="status-time">7:28 PM</div>
      <div class="status-right">
        <span>100%</span>
        <svg width="48" height="20" viewBox="0 0 48 20"><rect x="1" y="1" width="42" height="18" rx="3" fill="none" stroke="#fff" stroke-width="1.5"/><rect x="4" y="4" width="36" height="12" rx="1" fill="#fff"/><rect x="44.5" y="6" width="3" height="8" rx="1" fill="#fff"/></svg>
      </div>
    </div>
    <svg class="menu-icon" width="40" height="36" viewBox="0 0 40 36" stroke="#fff" stroke-width="2"><line x1="0" y1="2" x2="40" y2="2"/><line x1="0" y1="18" x2="40" y2="18"/><line x1="0" y1="34" x2="40" y2="34"/></svg>
    <h1 class="title">Dashboard</h1>
    <svg class="share-icon" width="40" height="48" viewBox="0 0 40 48" fill="none" stroke="#fff" stroke-width="2"><path d="M14 1 H1 V37 H39 V1 H26"/><line x1="20" y1="10" x2="20" y2="47"/><polyline points="12,18 20,10 28,18"/></svg>
  </header>

  <section class="tile overall">
    <div class="score">KV: 72</div>
    <div class="rank">
      <svg width="40" height="40" viewBox="0 0 40 40"><path fill="#fff" d="M20 1 L24 6 L30 4 L31 10 L37 12 L35 18 L39 22 L34 26 L35 32 L29 33 L26 38 L20 35 L14 38 L11 33 L5 32 L6 26 L1 22 L5 18 L3 12 L9 10 L10 4 L16 6 Z"/><circle cx="20" cy="20" r="10" fill="var(--overall)"/><path fill="#fff" d="M20 13 L22 18 L27 18 L23 21 L24.5 26 L20 23 L15.5 26 L17 21 L13 18 L18 18 Z"/></svg>
      <span>Rank 5 of 15</span>
    </div>
    <div class="comments">
      <svg width="26" height="24" viewBox="0 0 26 24" fill="#fff"><path d="M0 0 H16 V11 H5 L0 15 Z"/><path d="M9 8 H25 V19 H22 V24 L17 19 H9 Z" stroke="var(--overall)" stroke-width="1.5"/></svg>
      <span>14 Comments</span>
    </div>
    <div class="tile-label">OVERALL</div>
  </section>

  <section class="tile small bedside">
    <svg width="100" height="76" viewBox="0 0 100 76" fill="none" stroke="#fff" stroke-width="3"><line x1="2" y1="0" x2="2" y2="76"/><line x1="2" y1="46" x2="98" y2="46"/><line x1="98" y1="46" x2="98" y2="76"/><circle cx="13" cy="35" r="7" fill="#fff" stroke="none"/><rect x="24" y="33" width="74" height="9" rx="4" fill="#fff" stroke="none"/></svg>
    <div class="tile-label">BEDSIDE</div>
  </section>
  <section class="tile small knowledge">
    <svg width="104" height="100" viewBox="0 0 104 100" fill="none" stroke="#fff" stroke-width="3" stroke-linejoin="round"><path d="M52 12 C40 4 22 2 8 6 V82 C22 78 40 80 52 88 C64 80 82 78 96 82 V6 C82 2 64 4 52 12 Z"/><line x1="52" y1="12" x2="52" y2="88"/><path d="M8 14 H2 V90 H42 C44 96 60 96 62 90 H102 V14 H96"/></svg>
    <div class="tile-label">KNOWLEDGE</div>
  </section>
  <section class="tile small communication">
    <svg width="102" height="90" viewBox="0 0 102 90" fill="none" stroke="#fff" stroke-width="3" stroke-linejoin="round"><path d="M6 2 H96 A4 4 0 0 1 100 6 V64 A4 4 0 0 1 96 68 H82 L80 86 L64 68 H6 A4 4 0 0 1 2 64 V6 A4 4 0 0 1 6 2 Z"/><circle cx="36" cy="36" r="3.5" fill="#fff" stroke="none"/><circle cx="51" cy="36" r="3.5" fill="#fff" stroke="none"/><circle cx="66" cy="36" r="3.5" fill="#fff" stroke="none"/></svg>
    <div class="tile-label">COMMUNICATION</div>
  </section>

  <section class="tile wide time-spent">
    <svg width="104" height="104" viewBox="0 0 104 104" fill="none" stroke="#fff" stroke-width="3"><path d="M52 4 A49 49 0 1 1 26 11"/><line x1="52" y1="3" x2="52" y2="20"/><path d="M32 28 L55 48 L49 54 Z" fill="#fff" stroke-linejoin="round"/><circle cx="52" cy="51" r="4" fill="#fff" stroke="none"/></svg>
    <div class="tile-label">TIME SPENT</div>
  </section>
  <section class="tile wide outcome">
    <svg width="112" height="96" viewBox="0 0 112 96" fill="none" stroke="#fff" stroke-width="3" stroke-linejoin="round"><path d="M56 92 L20 56 C2 38 8 6 32 6 C44 6 52 14 56 20 C60 14 68 6 80 6 C104 6 110 38 92 56 Z"/><polyline points="2,46 40,46 46,36 52,62 58,22 64,56 70,42 76,50 110,50"/></svg>
    <div class="tile-label">OUTCOME</div>
  </section>
</main>
</body>
</html>
```